BSC Flyer to attract applicants 11x17

Brightline Stagecraft Company provides crew for local concerts, filming, theater, and corporate events.
The flyer will be posted on bulletin boards at colleges with theater programs.
Our primary venues are historic theaters in downtown LA
Need a 11x17 poster to attract potential applicants/crew
I have attached a poster that one of our staff made that has all if the relevant info - but i know the poster can look much better than that. I have also attached many images and our logo. It is not necessary to use all of the images, or any of them. The two images of the theater interiors are the venues we operate so they would be the first to include. I can send additional info or images upon request. Thank you

Entertainment

• APPLY@BSCCREWHUB.LA

```html
<!DOCTYPE html>
<html lang="en">
<head>
<meta charset="utf-8">
<title>Brightline Stagecraft Company – Open Positions</title>
<link rel="stylesheet" href="https://fonts.googleapis.com/css2?family=Montserrat:wght@300;600;700;800;900&display=swap">
<style>
  :root {
    --ink: #060608;
    --white: #ffffff;
    --blue: #2160b0;
    --blue-box: #1f5daa;
    --ghost: #3a3a3c;
    --label-bg: rgba(30, 30, 36, 0.8);
  }
  * { margin: 0; padding: 0; box-sizing: border-box; }
  html, body { width: 777px; height: 1200px; overflow: hidden; background: var(--ink); }
  .poster {
    position: relative; width: 777px; height: 1200px; overflow: hidden;
    background: var(--ink); color: var(--white);
    font-family: "Montserrat", Arial, sans-serif; text-align: center;
  }
  .photo { position: absolute; }
  .photo--theater-gold {
    left: 0; top: 0; width: 388px; height: 299px;
    background: radial-gradient(ellipse at 35% 35%, #e9b04a 0%, #b8711e 40%, #5a2a0c 80%),
                linear-gradient(90deg, #c88a2c, #b01818 95%);
  }
  .photo--console {
    left: 388px; top: 0; width: 389px; height: 299px;
    background: linear-gradient(160deg, #0b0b0d 0%, #2a2b2f 45%, #4b4c50 70%, #15161a 100%);
  }
  .photo--spotlight {
    left: 0; top: 299px; width: 388px; height: 301px;
    background: radial-gradient(ellipse at 20% 60%, #d6defa 0%, #5a62d8 30%, #2b2a8a 65%, #16164a 100%);
  }
  .photo--theater-ornate {
    left: 388px; top: 299px; width: 389px; height: 301px;
    background: radial-gradient(ellipse at 60% 10%, #d9a0d8 0%, #7a3a6a 25%, transparent 45%),
                radial-gradient(ellipse at 60% 60%, #e0b070 0%, #8a4a2a 35%, #2a1230 75%, #140a18 100%);
  }
  .brand-mark {
    position: absolute; left: 325px; top: 220px; width: 136px; height: 136px;
    border-radius: 50%; background: var(--ink); border: 6px solid var(--white);
    display: flex; align-items: center; justify-content: center;
    font-weight: 800; font-size: 40px; letter-spacing: 1px; color: var(--white);
  }
  .intro {
    position: absolute; left: 0; width: 777px; top: 466px;
    font-weight: 600; font-size: 28px; line-height: 34px; letter-spacing: 0.3px;
  }
  .intro span { background: var(--label-bg); padding: 0 8px; }
  .headline {
    position: absolute; left: 0; width: 777px; top: 540px;
    font-weight: 900; font-size: 97px; line-height: 88px; letter-spacing: -1px;
  }
  .pitch {
    position: absolute; left: 0; width: 777px; top: 734px;
    font-weight: 300; font-size: 31px; line-height: 40px; letter-spacing: 0.5px;
  }
  .rule { position: absolute; left: 355px; top: 921px; width: 79px; height: 4px; background: var(--blue); }
  .send-label {
    position: absolute; left: 0; width: 777px; top: 946px;
    font-weight: 800; font-size: 32px; color: var(--blue); letter-spacing: 0.3px;
  }
  .email-box {
    position: absolute; left: 191px; top: 992px; width: 400px; height: 61px;
    background: var(--blue-box); display: flex; align-items: center; justify-content: center;
    font-weight: 800; font-size: 26px; letter-spacing: 0.3px; color: var(--white);
  }
  .ghost-mark {
    position: absolute; left: 528px; top: 860px; width: 420px; height: 420px;
    border-radius: 50%; border: 26px solid var(--ghost);
    display: flex; align-items: center; justify-content: center;
    font-weight: 800; font-size: 120px; color: var(--ghost);
  }
  .site-line { position: absolute; top: 1140px; height: 3px; background: var(--blue); }
  .site-line--left { left: 0; width: 244px; }
  .site-line--right { left: 554px; width: 223px; }
  .site-url {
    position: absolute; left: 244px; width: 310px; top: 1124px;
    font-weight: 800; font-size: 24px; color: var(--blue);
  }
</style>
</head>
<body>
<main class="poster">
  <div class="photo photo--theater-gold" role="img" aria-label="Gilded historic theater interior with balconies and red stage curtain"></div>
  <div class="photo photo--console" role="img" aria-label="Lighting control console with screens"></div>
  <div class="photo photo--spotlight" role="img" aria-label="Follow spotlight rigged on chains with blue stage light beams"></div>
  <div class="photo photo--theater-ornate" role="img" aria-label="Ornate historic theater auditorium with carved proscenium and domed ceiling"></div>

  <div class="ghost-mark" aria-hidden="true">BSC</div>

  <div class="brand-mark">BSC</div>

  <p class="intro"><span>BRIGHTLINE STAGECRAFT</span><br>COMPANY HAS</p>
  <h1 class="headline">OPEN<br>POSITIONS</h1>
  <p class="pitch">WE ARE LOOKING FOR<br>TALENTED TECHNICIANS TO ADD<br>TO OUR ROSTER OF SKILLED<br>PROFESSIONALS.</p>

  <div class="rule"></div>
  <p class="send-label">SEND RESUME TO</p>
  <p class="email-box">APPLY@BSCCREWHUB.LA</p>

  <div class="site-line site-line--left"></div>
  <p class="site-url">WWW.BSCCREWHUB.LA</p>
  <div class="site-line site-line--right"></div>
</main>
</body>
</html>
```